Brightwell Systems - Company Overview Brochure

We would like a single page A4 Brochure to give to new potential customers to provide a quick overview of our company. This will be used in presales meetings.

We have included the content we would like on the brochure under "Brightwell Systems Marketing Brochure.docx".

We have included two other designs "timebundleterms v4.pdf and Brightwell Public Cloud Plans.pdf" which shows similar marketing brochures we have. We would like these designs to have the same Brightwell Blue and "Specialised Technology Consultancy firm" theme.

Target Market(s)

Technology Sector

Industry/Entity Type

Information Technology

Colors
0054AA
0677BA
7BADD7
CADEEF
E8F1F8

Requirements
Must have
• "Innovative Tech Company Theme".

```html
<!DOCTYPE html>
<html lang="en">
<head>
<meta charset="utf-8">
<title>Brightwell Systems – Company Overview</title>
<link rel="stylesheet" href="https://fonts.googleapis.com/css2?family=Inter:wght@400;500&family=Poppins:wght@600;700;800&display=swap">
<style>
  :root {
    --page-bg: #c2c2c2;
    --navy-deep: #1b2462;
    --navy: #22317a;
    --blue: #1d4fa8;
    --blue-bright: #0054aa;
    --teal: #1ba6c3;
    --white: #ffffff;
    --line: rgba(27, 166, 195, 0.55);
    --text: #f2f5fb;
  }
  * { box-sizing: border-box; margin: 0; padding: 0; }
  html, body { width: 862px; height: 1200px; overflow: hidden; }
  body { background: var(--page-bg); font-family: "Inter", Arial, sans-serif; color: var(--text); }

  .brochure {
    position: absolute; left: 7px; top: 0; width: 848px; height: 1200px; overflow: hidden;
    background: linear-gradient(160deg, var(--navy) 0%, #23408f 45%, var(--navy-deep) 100%);
  }
  .hero {
    position: absolute; left: 0; top: 0; width: 848px; height: 378px;
    background: linear-gradient(120deg, #1a2160 0%, #1f3f95 55%, #1d5dbb 100%);
  }
  .hero-art { position: absolute; right: 0; top: 0; width: 470px; height: 378px;
    background: radial-gradient(ellipse at 70% 40%, rgba(92,150,230,0.45), rgba(30,70,160,0) 70%); }

  .brand-band { position: absolute; left: 0; top: 37px; width: 472px; height: 85px; }
  .brand { position: absolute; left: 52px; top: 58px; display: flex; align-items: center; gap: 12px; }
  .brand-mark { width: 30px; height: 30px; background: var(--blue-bright); }
  .brand-name { font-family: "Poppins", Arial, sans-serif; font-weight: 700; font-size: 27px; color: var(--navy-deep); letter-spacing: 0.3px; }
  .brand-tag { position: absolute; left: 94px; top: 97px; font-family: "Inter", Arial, sans-serif; font-weight: 500; font-size: 13px; color: var(--teal); letter-spacing: 0.3px; }

  .slogan { position: absolute; left: 544px; top: 50px; font-family: "Poppins", Arial, sans-serif; font-weight: 800; font-size: 64px; line-height: 68px; letter-spacing: -1px; }
  .slogan .w { color: var(--white); display: block; }
  .slogan .t { color: var(--teal); display: block; }

  .intro { position: absolute; left: 51px; top: 224px; width: 330px; }
  .intro h1 { font-family: "Poppins", Arial, sans-serif; font-weight: 600; font-size: 23px; color: var(--teal); line-height: 30px; }
  .intro p { font-size: 15.5px; line-height: 20.5px; }

  .section-title { font-family: "Poppins", Arial, sans-serif; font-weight: 700; color: var(--teal); }
  .services-title { position: absolute; left: 0; width: 848px; top: 397px; text-align: center; font-size: 24px; }
  .rule { position: absolute; height: 2px; background: var(--white); }

  .services { position: absolute; left: 51px; top: 454px; display: grid; grid-template-columns: repeat(4, 172px); grid-auto-rows: 123px; column-gap: 19px; row-gap: 17px; }
  .service { border: 1px solid var(--line); border-radius: 6px; display: flex; flex-direction: column; align-items: center; justify-content: flex-end; padding-bottom: 10px; text-align: center; font-size: 14px; line-height: 17px; }
  .service svg { width: 62px; height: 62px; margin-bottom: 10px; fill: none; stroke: var(--white); stroke-width: 1.6; stroke-linecap: round; stroke-linejoin: round; }
  .service.two-line svg { margin-bottom: 6px; }

  .commitment { position: absolute; left: 51px; top: 740px; width: 330px; }
  .commitment h2, .policy h2 { font-size: 24px; line-height: 34px; }
  .commitment p { font-size: 14px; line-height: 17.1px; margin-top: 0; }
  .commitment p + p { margin-top: 17px; }
  .commitment .body { margin-top: 18px; }

  .policy { position: absolute; left: 451px; top: 740px; width: 346px; }
  .policy-card { position: absolute; left: 0; width: 346px; border: 1px solid rgba(255,255,255,0.45); border-top: none; border-radius: 0 0 12px 12px; padding: 10px 14px 12px 16px; font-size: 14px; line-height: 17.1px; }
  .policy-card::before { content: ""; position: absolute; left: 0; right: 0; top: 0; height: 12px; border-top: 1px solid rgba(255,255,255,0.45); border-left: 1px solid rgba(255,255,255,0.45); border-right: 1px solid rgba(255,255,255,0.45); border-radius: 12px 12px 0 0; clip-path: polygon(0 0, 7px 0, 7px 100%, 0 100%, 0 0, 0 0); }
  .policy-card .frame-top { position: absolute; top: 0; height: 1px; background: rgba(255,255,255,0.45); }
  .policy-label { position: absolute; font-family: "Poppins", Arial, sans-serif; font-weight: 600; font-size: 15px; color: var(--teal); left: 15px; }

  .footer-rule { position: absolute; left: 51px; top: 1124px; width: 602px; height: 1px; background: rgba(255,255,255,0.3); }
  .footer { position: absolute; left: 51px; top: 1135px; font-size: 12px; line-height: 16px; width: 620px; }
  .footer a { color: var(--teal); text-decoration: none; font-weight: 500; }
  .bottom-band { position: absolute; left: 0; bottom: 0; width: 848px; height: 12px; background: linear-gradient(90deg, #2a2870 0%, #1d6fc4 50%, #2a2870 100%); }
</style>
</head>
<body>
<main class="brochure">
  <section class="hero">
    <div class="hero-art" role="img" aria-label="Abstract blue network and angular light decoration"></div>
  </section>

  <svg class="brand-band" viewBox="0 0 472 85" aria-hidden="true"><polygon points="0,0 472,0 403,85 0,85" fill="#ffffff"/></svg>
  <div class="brand"><span class="brand-mark"></span><span class="brand-name">Brightwell Systems</span></div>
  <div class="brand-tag">SPECIALISED CONSULTING</div>

  <h2 class="slogan"><span class="w">Do it</span><span class="t">Once,</span><span class="w">Do it</span><span class="t">Right</span></h2>

  <section class="intro">
    <h1>Brightwell Systems</h1>
    <p>is a Technology Consulting Company based in Perth, Western Australia, which offers customers tailored technical solutions for a range of products.</p>
  </section>

  <h2 class="section-title services-title">OUR SERVICES</h2>
  <div class="rule" style="left:401px; top:434px; width:46px;"></div>

  <section class="services">
    <div class="service">
      <svg viewBox="0 0 64 64"><path d="M10 40h44M16 40V24h8v16M26 40V14h10v26M38 40V20h8v20M48 40V28h6"/><path d="M8 40a24 12 0 0 0 48 0"/><path d="M20 50l-2 4M32 52v5M44 50l2 4"/></svg>
      <span>Project Integration</span>
    </div>
    <div class="service">
      <svg viewBox="0 0 64 64"><circle cx="20" cy="18" r="7"/><circle cx="40" cy="22" r="9"/><circle cx="40" cy="20" r="3"/><path d="M34 28a6 5 0 0 1 12 0"/><path d="M8 46l10-6h12l4 4H22M18 52l6 4h16l16-12-4-3-14 8"/></svg>
      <span>Managed Services</span>
    </div>
    <div class="service">
      <svg viewBox="0 0 64 64"><path d="M32 8l16 6v14c0 12-7 20-16 26-9-6-16-14-16-26V14z"/><circle cx="32" cy="28" r="4"/><path d="M30 32l-1 7h6l-1-7"/><path d="M10 12l6 2M54 12l-6 2"/></svg>
      <span>Enterprise Security</span>
    </div>
    <div class="service">
      <svg viewBox="0 0 64 64"><rect x="6" y="12" width="40" height="28" rx="2"/><path d="M22 46h12M28 40v6"/><path d="M18 22l-4 4 4 4M34 22l4 4-4 4M28 20l-4 12"/><circle cx="48" cy="40" r="8"/><circle cx="48" cy="40" r="3"/></svg>
      <span>Software Development</span>
    </div>
    <div class="service">
      <svg viewBox="0 0 64 64"><path d="M8 18l34-8 6 18-34 8z"/><ellipse cx="11" cy="27" rx="4" ry="9"/><path d="M40 30l6 10h6v14M46 40v8"/></svg>
      <span>CCTV</span>
    </div>
    <div class="service two-line">
      <svg viewBox="0 0 64 64"><path d="M32 12l12 5v10c0 9-5 15-12 19-7-4-12-10-12-19V17z"/><circle cx="32" cy="27" r="3"/><path d="M32 30v6M20 22H10v-8M44 22h10v-8M20 34H10v10M44 34h10v10M32 46v8"/><circle cx="10" cy="12" r="2"/><circle cx="54" cy="12" r="2"/><circle cx="10" cy="46" r="2"/><circle cx="54" cy="46" r="2"/></svg>
      <span>Integrated<br>Electronic Security</span>
    </div>
    <div class="service two-line">
      <svg viewBox="0 0 64 64"><path d="M8 10c4 20 18 30 30 30M6 20c6 16 18 24 28 24M14 8c6 14 14 20 26 26"/><circle cx="44" cy="30" r="2"/><circle cx="50" cy="34" r="2"/><circle cx="46" cy="38" r="2"/><circle cx="52" cy="42" r="2"/><circle cx="44" cy="46" r="2"/></svg>
      <span>Structured Cabling<br>and Fibre Optics</span>
    </div>
    <div class="service two-line">
      <svg viewBox="0 0 64 64"><circle cx="32" cy="24" r="4"/><path d="M24 32a11 11 0 1 1 16 0M18 38a19 19 0 1 1 28 0"/><path d="M32 28l-10 26M32 28l10 26M26 44h12"/></svg>
      <span>Wireless<br>Communications</span>
    </div>
  </section>

  <section class="commitment">
    <h2 class="section-title">Our Commitment</h2>
    <div class="body">
      <p>Our commitment to you is to do things right the first time while being fair but cost-effective. If you’re looking for the cheapest consultants, Brightwell may not be the right fit for you.</p>
      <p>We are a specialised consultancy firm that offers tailored solutions to government and the enterprise sector with some of Perth's best consultants.</p>
      <p>In areas such as cybersecurity and business continuity, it pays to get it done correctly the first time in alignment with vendor best practices. There are many ways of doing things in the technology field, and only after understanding all methods of achieving an outcome can you recommend the best solution in alignment with best practices.</p>
    </div>
  </section>
  <div class="rule" style="left:51px; top:781px; width:47px;"></div>

  <section class="policy">
    <h2 class="section-title">Our Policy</h2>
    <div class="policy-card" style="top:61px; height:145px;">
      <span class="frame-top" style="left:0; width:12px;"></span><span class="frame-top" style="left:73px; right:0;"></span>
      “At Brightwell we believe that both parties benefit when pricing is fair. If margins are too low, we may sacrifice service quality, and this ultimately harms our brand. If margins are too high, our customers have an incentive to seek alternative providers, and this compromises our growth and damages client relationships.”
    </div>
    <span class="policy-label" style="top:49px;">Be Fair</span>
    <div class="policy-card" style="top:248px; height:86px;">
      <span class="frame-top" style="left:0; width:12px;"></span><span class="frame-top" style="left:150px; right:0;"></span>
      “At Brightwell we believe that it is possible to deliver both high quality at a fair cost, by providing services that are intelligent and efficient.”
    </div>
    <span class="policy-label" style="top:236px;">Be Cost-Effective</span>
  </section>
  <div class="rule" style="left:451px; top:781px; width:47px;"></div>

  <div class="footer-rule"></div>
  <p class="footer">All goods and services provided by Brightwell are provided in accordance with our Standard Terms and Conditions available at <a href="https://www.brightwellsystems.com.au/t&amp;c">https://www.brightwellsystems.com.au/t&amp;c</a></p>
  <div class="bottom-band"></div>
</main>
</body>
</html>
```